Stationary Design For New Dynamic Company

Hi there we require stationary designed for our new company, we have used "Pixel Harbor" recently for our logo and were very impressed with all of the designers that contributed towards the final result.
What we require now is the following:
Letter head layout (A4)
Business Cards (5 people)
With Compliments slips
Envelopes
Email stationary
We would like to use our current logo design and I have included it for your use (JPEG is the one we have chosen and I have attached an EPS file for your use). Our company specializes in architectural cladding and our products are used by architects, builders and private clients, so we wish for the stationary to be suitable and attractive to our clientele.
I thank everyone in advance for your contributions.
Thank you to all that have provided your designs for this project, I apologize for not providing feedback as I have been away. I have looked at everyone's designs and they all look great and I will come back to those designers that I wish to have changes made sometime today.
Once again a big thank you to all involved.
Business

```html
<!DOCTYPE html>
<html lang="en">
<head>
<meta charset="utf-8">
<title>Stonevale Business Card</title>
<link rel="stylesheet" href="https://fonts.googleapis.com/css2?family=Source+Sans+3:wght@400;600;700&display=swap">
<style>
  :root {
    --navy: #27286e;
    --orange: #f5821f;
    --ink: #1c1c1c;
    --card: #ffffff;
    --backdrop: #8e8e8e;
  }
  * { box-sizing: border-box; margin: 0; padding: 0; }
  html, body { width: 1200px; height: 900px; overflow: hidden; }
  body {
    background: var(--backdrop);
    font-family: "Source Sans 3", Arial, sans-serif;
  }
  .canvas {
    position: relative;
    width: 1200px;
    height: 900px;
    display: flex;
    align-items: center;
    justify-content: center;
    gap: 60px;
  }
  .card {
    position: relative;
    width: 525px;
    height: 300px;
    background: var(--card);
    overflow: hidden;
    box-shadow: 0 6px 18px rgba(0,0,0,0.25);
  }
  .card-swoosh {
    position: absolute;
    inset: 0;
    width: 100%;
    height: 100%;
  }
  .brand {
    position: absolute;
    top: 30px;
    left: 28px;
    display: flex;
    align-items: center;
    gap: 10px;
  }
  .brand-square {
    width: 22px;
    height: 22px;
    background: var(--navy);
  }
  .brand-name {
    font-size: 31px;
    font-weight: 700;
    color: var(--navy);
    letter-spacing: 0.5px;
  }
  .contact {
    position: absolute;
    top: 30px;
    right: 28px;
    text-align: right;
    font-size: 16px;
    line-height: 21px;
    color: var(--ink);
  }
  .contact-name { color: var(--navy); font-weight: 400; }
  .contact-gap { height: 21px; }
  .contact-web {
    position: absolute;
    right: 28px;
    bottom: 36px;
    font-size: 16px;
    color: var(--orange);
  }
  .card-back {
    display: flex;
    align-items: center;
    justify-content: center;
  }
  .card-back .brand {
    position: static;
    gap: 16px;
  }
  .card-back .brand-square { width: 34px; height: 34px; }
  .card-back .brand-name { font-size: 52px; }
</style>
</head>
<body>
  <main class="canvas">
    <section class="card card-front">
      <svg class="card-swoosh" viewBox="0 0 525 300" aria-hidden="true">
        <path d="M 302 0 C 318 140 230 260 40 300 L 100 300 C 268 250 330 140 302 0 Z" fill="var(--orange)"/>
      </svg>
      <div class="brand">
        <span class="brand-square"></span>
        <span class="brand-name">STONEVALE</span>
      </div>
      <div class="contact">
        <p class="contact-name">FULL NAME</p>
        <p>The Job Title</p>
        <p>email@stonevale.com</p>
        <p>01234546789</p>
        <div class="contact-gap"></div>
        <p>01234567890</p>
        <p>1 Street Address</p>
        <p>Yourcity</p>
        <p>1234</p>
      </div>
      <p class="contact-web">www.stonevale.com</p>
    </section>

    <section class="card card-back">
      <div class="brand">
        <span class="brand-square"></span>
        <span class="brand-name">STONEVALE</span>
      </div>
    </section>
  </main>
</body>
</html>
```